I have a PHP web application to manage IT support calls and require a front-end design and user logon screen.

I have attached the current design which needs improving.

I have 2 current designs. The 2nd design is one I have been working on but requires a "professional touch". I also require the tables designed with dummy data from the 1st design.

I have attached my company logo in AI format which I would like incorporated into the design. There should also be a placeholder to supply the users company name upon login.

The screenshots I have attached should explain what I am looking for.

The Home Page should include charts which show statistical information such as:
Number of support tickets logged per month. Bar Chart etc.
Number of currently open support tickets.
Number of Quote Requests awaiting a response.
Number of Files and file repository.
Number of Reports.
Number of Customers.

For the Jobs and Customers pages the table fields should be designed as per the attached screenshots but a better looking tables. The table options such as uploading a file and adding a customer - these options can be changed and displayed differently.

Quotes page should display quotes returned and a "request a quote form".

Files page should have a good structure for browsing through an archive of files.

Profile page should have the option to include a profile picture.

An additional side page should be created for a web based calendar (these calendar entries will be updated by code).

The navbar should also include an alerts section.
The current attached design I have is based on bootstraps navbar.

Inspiration: http://plenvaro.com/freebie/free-admin-templates-for-backend-panels/

Hopefully this above link will show you some navigation style designs that I am looking for.

Please note, I will be doing the PHP coding myself and it is just the page designs I require in either HTML and or PHP format. I also require the CSS files for this project.
I need the code in a format where I can add and remove items in the menu from the code and not PSD/image based format.

If you think this project requires a higher budget let me know what you would expect and I will increase it!

Any questions, please let me know.
Dummy data can be shown for design purposes.

I have provided you a dummy login to our current system to show you the system:
https://reef.vomilbrixtonsolutions.co.uk/
username: dan.hollow@vomilbrixtonsolutions.co.uk
password:K#72zqTm

```html
<!DOCTYPE html>
<html lang="en">
<head>
<meta charset="utf-8">
<title>Support Desk Dashboard</title>
<link href="https://fonts.googleapis.com/css2?family=Open+Sans:wght@400;600&family=Roboto+Condensed:wght@400;700&display=swap" rel="stylesheet">
<style>
:root{
  --sidebar:#232a35;
  --brand:#1f4e9e;
  --page:#e8ebee;
  --panel:#ffffff;
  --line:#e3e6ea;
  --text:#4a4f57;
  --muted:#a8b0c4;
  --green:#5cb85c;
  --red:#e0474c;
  --blue:#3ab0e2;
  --orange:#f6a623;
  --navy:#1f4e9e;
  --dark:#2b2f36;
}
*{box-sizing:border-box;margin:0;padding:0}
html,body{width:1167px;height:1200px;overflow:hidden;background:var(--page)}
body{font-family:"Open Sans",sans-serif;color:var(--text)}
.app{position:relative;width:1400px;height:1440px;transform:scale(.83357);transform-origin:0 0;background:var(--page)}
.abs{position:absolute}
/* sidebar */
.sidebar{left:0;top:0;width:307px;height:1440px;background:var(--sidebar)}
.brand{height:135px;background:var(--brand);display:flex;align-items:center;padding-left:36px;gap:14px}
.brand-dot{width:38px;height:38px;border-radius:50%;border:4px solid #fff}
.brand-name{color:#fff;font-size:25px;font-weight:600;line-height:1.1}
.search{position:absolute;left:27px;top:155px;width:254px;height:32px;background:#2d3440;border:1px solid #3a414d;color:#9aa2ad;font-size:12px;padding:7px 11px}
.search svg{position:absolute;right:12px;top:9px}
.menu{position:absolute;top:222px;left:0;list-style:none;width:100%}
.menu li{height:38px;display:flex;align-items:center;padding-left:29px;color:#c8cdd4;font-size:13px;gap:18px}
.menu svg{width:14px;height:14px}
/* topbar */
.topbar{left:307px;top:0;width:1093px;height:48px;background:#fff}
.lang{position:absolute;left:55px;top:15px;font-size:14px;color:#555}
.badge{position:absolute;top:10px;width:20px;height:20px;border-radius:50%;background:var(--red);color:#fff;font-size:10px;text-align:center;line-height:20px;font-weight:600}
.user{position:absolute;left:936px;top:15px;font-size:18px;color:#444}
/* cards */
.card{background:var(--panel);top:83px;width:229px;height:168px}
.card .ic{position:absolute;left:22px;top:23px;width:50px;height:50px;border-radius:50%}
.card h3{position:absolute;left:82px;top:50px;font-size:15px;font-weight:400;color:#555}
.card .track{position:absolute;left:13px;top:93px;width:197px;height:4px;background:#eef0f2}
.card .fill{height:4px}
.card p{position:absolute;left:12px;top:117px;font-size:13px;color:#555}
.panel{background:var(--panel)}
.ph{font-size:16px;color:#444}
/* statistic */
.seg{position:absolute;left:406px;top:74px;display:flex;border:1px solid #ccc;font-size:12px}
.seg span{padding:2px 5px;border-right:1px solid #ccc;color:#333}
.seg span:last-child{border-right:0}
/* calendar */
.cal-head{height:48px;border-bottom:1px solid var(--line);text-align:center;line-height:48px;font-size:15px;color:#333;position:relative}
.grid{display:grid;grid-template-columns:repeat(7,1fr);font-family:"Roboto Condensed",sans-serif}
.wd{height:50px;background:#eef0f3;border-right:1px solid #dfe2e6;text-align:center;line-height:50px;font-size:14px;color:#333}
.day{height:61px;border-right:1px solid #e6e8eb;border-bottom:1px solid #e6e8eb;text-align:center;position:relative}
.day b{display:block;font-size:19px;color:#1d2a44;padding-top:16px}
.day i{position:absolute;left:0;right:0;bottom:-6px;font-style:normal;font-size:13px;color:var(--muted)}
.day.off{background:#f2f3f6}.day.off b{color:#d3d8e2}
.day.ghost b{color:#e0e4ea}.day.ghost i{color:#ccd2dd}
.day.mark{background:#e4e8ef}.day.today b{color:#3a94d2}
/* reports */
.rtable{position:absolute;left:16px;top:57px;width:448px;border-collapse:collapse;font-family:"Roboto Condensed",sans-serif;font-size:12px;color:#333}
.rtable th{text-align:left;font-size:13px;padding:12px 8px;border-bottom:2px solid #ddd}
.rtable td{padding:0 8px;height:34px;border-bottom:1px solid #e6e6e6}
.bar{width:83px;height:8px;background:#eceff3}.bar div{height:8px}
.stat{width:145px;height:62px;background:#fff;border:1px solid #dde1e6}
.stat h4{position:absolute;left:17px;top:13px;font-size:12px;font-weight:600;color:var(--navy)}
.stat span{position:absolute;left:16px;top:33px;font-size:17px;color:#555;display:flex;align-items:center;gap:6px}
.footer{left:351px;top:1406px;font-size:13px;color:#333}
</style>
</head>
<body>
<div class="app">

<aside class="abs sidebar">
  <div class="brand"><div class="brand-dot"></div><div class="brand-name">Vomil Brixton<br>Solutions</div></div>
  <div class="search">Search here...
    <svg width="14" height="14" viewBox="0 0 14 14"><circle cx="6" cy="6" r="4.5" fill="none" stroke="#9aa2ad" stroke-width="2"/><line x1="9" y1="9" x2="13" y2="13" stroke="#9aa2ad" stroke-width="2"/></svg>
  </div>
  <ul class="menu">
    <li><svg viewBox="0 0 14 14"><path d="M1 7L7 1l6 6h-2v6H8V9H6v4H3V7z" fill="#c8cdd4"/></svg>Home</li>
    <li><svg viewBox="0 0 14 14"><rect x="1" y="2" width="12" height="10" fill="none" stroke="#c8cdd4"/><rect x="3" y="7" width="2" height="4" fill="#c8cdd4"/><rect x="6" y="5" width="2" height="6" fill="#c8cdd4"/><rect x="9" y="4" width="2" height="7" fill="#c8cdd4"/></svg>Jobs</li>
    <li><svg viewBox="0 0 14 14"><ellipse cx="7" cy="8" rx="4" ry="5" fill="#c8cdd4"/><circle cx="7" cy="2.5" r="2" fill="#c8cdd4"/></svg>Customers</li>
    <li><svg viewBox="0 0 14 14"><path d="M4 3L1 7l3 4M10 3l3 4-3 4M8 2L6 12" fill="none" stroke="#c8cdd4" stroke-width="1.5"/></svg>Chart</li>
    <li><svg viewBox="0 0 14 14"><rect x="1" y="3" width="10" height="10" fill="none" stroke="#c8cdd4" stroke-width="1.5"/><path d="M6 9l7-7" stroke="#c8cdd4" stroke-width="2"/></svg>Inventory</li>
    <li><svg viewBox="0 0 14 14"><rect x="1" y="2" width="12" height="10" fill="none" stroke="#c8cdd4" stroke-width="1.5"/><path d="M1 5.5h12M1 8.5h12M5 2v10M9 2v10" stroke="#c8cdd4"/></svg>Quote</li>
    <li><svg viewBox="0 0 14 14"><circle cx="7" cy="7" r="5.5" fill="none" stroke="#c8cdd4" stroke-width="1.5"/><path d="M4.5 8.5q2.5 2.5 5 0" fill="none" stroke="#c8cdd4"/></svg>Files</li>
    <li><svg viewBox="0 0 14 14"><rect x="1" y="3" width="12" height="9" fill="#c8cdd4"/><path d="M1 3l6 5 6-5" fill="none" stroke="#232a35"/></svg>Reports</li>
  </ul>
</aside>

<header class="abs topbar">
  <svg class="abs" style="left:13px;top:17px" width="12" height="12" viewBox="0 0 12 12"><circle cx="6" cy="6" r="4" fill="none" stroke="#555" stroke-width="2.5" stroke-dasharray="2 1.2"/></svg>
  <div class="lang">English (US) ⌄</div>
  <svg class="abs" style="left:830px;top:22px" width="14" height="15" viewBox="0 0 14 15"><path d="M7 1a4 4 0 014 4v4l2 3H1l2-3V5a4 4 0 014-4zM5 13h4a2 2 0 01-4 0z" fill="#333"/></svg>
  <div class="badge" style="left:840px">24</div>
  <svg class="abs" style="left:873px;top:25px" width="14" height="11" viewBox="0 0 14 11"><rect width="14" height="11" fill="#333"/><path d="M0 0l7 6 7-6" fill="none" stroke="#fff"/></svg>
  <div class="badge" style="left:884px">24</div>
  <div class="user">Dan Hollow ⌄</div>
</header>

<div class="abs card" style="left:344px"><div class="ic" style="background:var(--green)"></div><h3>CUSTOMERS</h3><div class="track"><div class="fill" style="width:158px;background:var(--green)"></div></div><p>Lorem lipsum is a simply dummy</p></div>
<div class="abs card" style="left:603px"><div class="ic" style="background:var(--red)"></div><h3>JOBS</h3><div class="track"><div class="fill" style="width:128px;background:var(--red)"></div></div><p>Lorem lipsum is a simply dummy</p></div>
<div class="abs card" style="left:861px"><div class="ic" style="background:var(--blue)"></div><h3>QUOTE</h3><div class="track"><div class="fill" style="width:187px;background:var(--blue)"></div></div><p>Lorem lipsum is a simply dummy</p></div>
<div class="abs card" style="left:1120px"><div class="ic" style="background:var(--orange)"></div><h3>REPORTS</h3><div class="track"><div class="fill" style="width:108px;background:var(--orange)"></div></div><p>Lorem lipsum is a simply dummy</p></div>

<section class="abs panel" style="left:344px;top:290px;width:655px;height:318px">
  <div class="ph" style="position:absolute;left:20px;top:19px">Statistic</div>
  <div style="position:absolute;left:0;right:0;top:53px;border-top:1px solid var(--line)"></div>
  <div class="seg"><span>All time</span><span>This year</span><span>This month</span><span>Today</span></div>
  <svg class="abs" style="left:0;top:0" width="655" height="318" viewBox="344 290 655 318" font-family="Open Sans,sans-serif" font-size="12" fill="#555">
    <g stroke="#e5e5e5"><line x1="405" y1="410" x2="960" y2="410"/><line x1="405" y1="444" x2="960" y2="444"/><line x1="405" y1="477" x2="960" y2="477"/><line x1="405" y1="511" x2="960" y2="511"/><line x1="405" y1="545" x2="960" y2="545"/></g>
    <g text-anchor="end"><text x="396" y="414">500</text><text x="396" y="448">375</text><text x="396" y="481">250</text><text x="396" y="515">125</text><text x="396" y="549">0</text></g>
    <g text-anchor="middle"><text x="408" y="570">2006</text><text x="477" y="570">2007</text><text x="546" y="570">2008</text><text x="615" y="570">2009</text><text x="684" y="570">2010</text><text x="752" y="570">2011</text><text x="821" y="570">2012</text><text x="890" y="570">2013</text><text x="959" y="570">2014</text></g>
    <polygon points="408,462 477,481 546,499 615,481 684,500 752,477 821,457 890,439 959,424 959,545 408,545" fill="#dc3535"/>
    <polygon points="408,494 477,507 546,521 615,507 684,521 752,507 821,494 890,481 959,469 959,545 408,545" fill="#e8cc4a"/>
    <polygon points="408,518 477,525 546,531 615,525 684,531 752,525 821,518 890,511 959,506 959,545 408,545" fill="#9cc98e"/>
    <polyline points="408,462 477,481 546,499 615,481 684,500 752,477 821,457 890,439 959,424" fill="none" stroke="#c81f1f" stroke-width="2"/>
    <polyline points="408,494 477,507 546,521 615,507 684,521 752,507 821,494 890,481 959,469" fill="none" stroke="#f3c400" stroke-width="2"/>
    <polyline points="408,518 477,525 546,531 615,525 684,531 752,525 821,518 890,511 959,506" fill="none" stroke="#4caf50" stroke-width="2"/>
    <g fill="#fff" stroke="#c81f1f" stroke-width="1.5"><circle cx="408" cy="462" r="3.5"/><circle cx="477" cy="481" r="3.5"/><circle cx="546" cy="499" r="3.5"/><circle cx="684" cy="500" r="3.5"/><circle cx="752" cy="477" r="3.5"/><circle cx="821" cy="457" r="3.5"/><circle cx="890" cy="439" r="3.5"/><circle cx="959" cy="424" r="3.5" fill="#c81f1f"/></g>
    <g fill="#fff" stroke="#f3c400" stroke-width="1.5"><circle cx="408" cy="494" r="3.5"/><circle cx="477" cy="507" r="3.5"/><circle cx="546" cy="521" r="3.5"/><circle cx="615" cy="507" r="6" fill="#f3c400"/><circle cx="684" cy="521" r="3.5"/><circle cx="752" cy="507" r="3.5"/><circle cx="821" cy="494" r="3.5"/><circle cx="890" cy="481" r="3.5"/><circle cx="959" cy="469" r="3.5"/></g>
    <g fill="#fff" stroke="#4caf50" stroke-width="1.5"><circle cx="408" cy="518" r="3.5"/><circle cx="477" cy="525" r="3.5"/><circle cx="546" cy="531" r="3.5"/><circle cx="615" cy="525" r="6" fill="#4caf50"/><circle cx="684" cy="531" r="3.5"/><circle cx="752" cy="525" r="3.5"/><circle cx="821" cy="518" r="3.5"/><circle cx="890" cy="511" r="3.5"/><circle cx="959" cy="506" r="3.5"/></g>
    <rect x="567" y="400" width="96" height="92" rx="5" fill="#fff" fill-opacity=".88" stroke="#e6e6e6"/>
    <g text-anchor="middle"><text x="615" y="423" fill="#333" font-weight="600">2009</text><text x="615" y="440" fill="#4caf50">Customers: 150</text><text x="615" y="461" fill="#f3c400">Visitor: 65</text><text x="615" y="479" fill="#c81f1f">Page Hits: 96</text></g>
  </svg>
</section>

<section class="abs panel" style="left:1016px;top:290px;width:333px;height:318px">
  <div role="img" aria-label="Landscape photo of a fjord with green mountains and waterfalls" style="height:148px;background:linear-gradient(180deg,#c6cfd8 0%,#6d8a5a 45%,#3f8f98 100%)"></div>
  <div role="img" aria-label="Profile photo of Dan Hollow" style="position:absolute;left:112px;top:90px;width:108px;height:108px;border-radius:50%;border:5px solid #fff;background:linear-gradient(180deg,#6b4a35,#c99a7c)"></div>
  <div style="position:absolute;left:0;right:0;top:206px;text-align:center;font-size:18px;color:#555">Dan Hollow</div>
  <div style="position:absolute;left:23px;top:263px;width:127px;height:32px;background:#2b2b2b;color:#fff;font-size:13px;text-align:center;line-height:32px">● View Profile</div>
  <div style="position:absolute;left:178px;top:263px;width:129px;height:32px;border:1px solid #555;color:#333;font-size:13px;text-align:center;line-height:30px">● Edit Profile</div>
</section>

<section class="abs panel" style="left:344px;top:632px;width:479px;height:463px;overflow:hidden">
  <div class="cal-head"><span style="position:absolute;left:24px">‹</span>May 2014<span style="position:absolute;right:24px">›</span></div>
  <div class="grid">
    <div class="wd">Sun</div><div class="wd">Mon</div><div class="wd">Tue</div><div class="wd">Wed</div><div class="wd">Thu</div><div class="wd">Fri</div><div class="wd">Sat</div>
    <div class="day off"><b>27</b><i>Busy</i></div><div class="day ghost"><b>28</b><i>Available</i></div><div class="day off"><b>29</b><i>Busy</i></div><div class="day ghost"><b>30</b><i>Available</i></div><div class="day"><b>1</b><i>Available</i></div><div class="day"><b>2</b><i>Available</i></div><div class="day"><b>3</b><i>Available</i></div>
    <div class="day"><b>4</b><i>Available</i></div><div class="day mark"><b>5</b><i>Busy</i></div><div class="day"><b>6</b><i>Available</i></div><div class="day"><b>7</b><i>Available</i></div><div class="day"><b>8</b><i>Available</i></div><div class="day"><b>9</b><i>Available</i></div><div class="day"><b>10</b><i>Available</i></div>
    <div class="day"><b>11</b><i>Available</i></div><div class="day mark"><b>12</b><i>Busy</i></div><div class="day"><b>13</b><i>Available</i></div><div class="day mark today"><b>14</b><i>Busy</i></div><div class="day mark"><b>15</b><i>Busy</i></div><div class="day"><b>16</b><i>Available</i></div><div class="day"><b>17</b><i>Available</i></div>
    <div class="day"><b>18</b><i>Available</i></div><div class="day"><b>19</b><i>Available</i></div><div class="day"><b>20</b><i>Available</i></div><div class="day"><b>21</b><i>Available</i></div><div class="day"><b>22</b><i>Available</i></div><div class="day"><b>23</b><i>Available</i></div><div class="day mark"><b>24</b><i>Busy</i></div>
    <div class="day"><b>25</b><i>Available</i></div><div class="day"><b>26</b><i>Available</i></div><div class="day"><b>27</b><i>Available</i></div><div class="day"><b>28</b><i>Available</i></div><div class="day"><b>29</b><i>Available</i></div><div class="day"><b>30</b><i>Available</i></div><div class="day"><b>31</b><i>Available</i></div>
    <div class="day ghost"><b>1</b><i>Available</i></div><div class="day ghost"><b>2</b><i>Available</i></div><div class="day ghost"><b>3</b><i>Available</i></div><div class="day ghost"><b>4</b><i>Available</i></div><div class="day ghost"><b>5</b><i>Available</i></div><div class="day ghost"><b>6</b><i>Available</i></div><div class="day ghost"><b>7</b><i>Available</i></div>
  </div>
</section>

<section class="abs panel" style="left:344px;top:1111px;width:479px;height:275px">
  <div style="height:41px;background:var(--navy);color:#fff;font-size:16px;padding:11px 13px">Tickets</div>
  <svg class="abs" style="left:0;top:0" width="479" height="275" viewBox="344 1111 479 275" font-family="Open Sans,sans-serif" font-size="8" fill="#444">
    <g stroke="#dadada"><line x1="378" y1="1177" x2="811" y2="1177"/><line x1="378" y1="1214" x2="811" y2="1214"/><line x1="378" y1="1251" x2="811" y2="1251"/><line x1="378" y1="1289" x2="811" y2="1289"/><line x1="378" y1="1326" x2="811" y2="1326"/><line x1="378" y1="1363" x2="811" y2="1363"/></g>
    <g text-anchor="end"><text x="373" y="1180">12500</text><text x="373" y="1217">10000</text><text x="373" y="1254">7500</text><text x="373" y="1292">5000</text><text x="373" y="1329">2500</text><text x="373" y="1366">0</text></g>
    <g text-anchor="middle"><text x="392" y="1375">2</text><text x="422" y="1375">4</text><text x="452" y="1375">6</text><text x="482" y="1375">8</text><text x="512" y="1375">10</text><text x="542" y="1375">12</text><text x="572" y="1375">14</text><text x="602" y="1375">16</text><text x="632" y="1375">18</text><text x="662" y="1375">20</text><text x="692" y="1375">22</text><text x="722" y="1375">24</text><text x="752" y="1375">26</text><text x="782" y="1375">28</text><text x="811" y="1375">30</text></g>
    <polygon points="378,1245 392,1262 407,1245 422,1183 437,1260 452,1212 467,1222 482,1235 497,1257 512,1187 527,1203 542,1232 557,1228 572,1217 587,1222 602,1240 617,1195 632,1183 647,1212 662,1222 677,1247 692,1235 707,1203 722,1197 737,1240 752,1232 767,1212 782,1192 797,1197 811,1215 811,1363 378,1363" fill="#eef7dc" fill-opacity=".8"/>
    <polyline points="378,1245 392,1262 407,1245 422,1183 437,1260 452,1212 467,1222 482,1235 497,1257 512,1187 527,1203 542,1232 557,1228 572,1217 587,1222 602,1240 617,1195 632,1183 647,1212 662,1222 677,1247 692,1235 707,1203 722,1197 737,1240 752,1232 767,1212 782,1192 797,1197 811,1215" fill="none" stroke="#c8e6a0"/>
    <polygon points="378,1262 392,1197 407,1257 422,1240 437,1272 452,1217 467,1225 482,1235 497,1275 512,1201 527,1272 542,1195 557,1272 572,1232 587,1255 602,1200 617,1260 632,1215 647,1225 662,1217 677,1195 692,1215 707,1232 722,1260 737,1225 752,1205 767,1272 782,1227 797,1188 811,1217 811,1363 378,1363" fill="#cfece9" fill-opacity=".55"/>
    <polyline points="378,1262 392,1197 407,1257 422,1240 437,1272 452,1217 467,1225 482,1235 497,1275 512,1201 527,1272 542,1195 557,1272 572,1232 587,1255 602,1200 617,1260 632,1215 647,1225 662,1217 677,1195 692,1215 707,1232 722,1260 737,1225 752,1205 767,1272 782,1227 797,1188 811,1217" fill="none" stroke="#7cc6e3"/>
  </svg>
</section>

<section class="abs panel" style="left:869px;top:632px;width:479px;height:291px;border:1px solid #e3e6ea">
  <div style="height:40px;border-bottom:1px solid var(--line);padding:10px 16px" class="ph"><span style="color:#c8cdd4">✓</span> Reports<span style="float:right;color:#ccd;font-size:14px">⌃ &nbsp; ✕</span></div>
  <table class="rtable">
    <tr><th>Task ▲</th><th>Assigned to</th><th>Progress</th><th>Status</th></tr>
    <tr><td>A/B Tests</td><td>Vera Lund</td><td><div class="bar"><div style="width:60px;background:#f33"></div></div></td><td style="color:var(--red)">Canceled</td></tr>
    <tr><td>App Development</td><td>Paul Reyes</td><td><div class="bar"><div style="width:79px;background:#4aa628"></div></div></td><td style="color:#4aa628">Active</td></tr>
    <tr><td>Growth Hacking</td><td>Owen Marsh</td><td><div class="bar"><div style="width:8px;background:#2a7bd1"></div></div></td><td style="color:#2a7bd1">Active</td></tr>
    <tr><td>Hire Developers</td><td>Nina Ford</td><td><div class="bar"><div style="width:22px;background:var(--orange)"></div></div></td><td style="color:var(--orange)">Pending</td></tr>
    <tr><td>SEO Optimisation</td><td>Theo Grant</td><td><div class="bar"><div style="width:60px;background:var(--blue)"></div></div></td><td style="color:var(--blue)">Active</td></tr>
  </table>
</section>

<section class="abs panel" style="left:869px;top:941px;width:479px;height:241px;border:1px solid #e3e6ea">
  <div style="height:41px;border-bottom:1px solid var(--line);padding:10px 44px;font-family:'Roboto Condensed',sans-serif" class="ph">Weekly Stat<span style="float:right;color:#ccd;font-size:14px">⌃ &nbsp; ✕</span></div>
  <svg class="abs" style="left:0;top:0" width="479" height="241" viewBox="869 941 479 241" font-family="Open Sans,sans-serif" font-size="9" fill="#333">
    <g stroke="#e4e4e4"><line x1="899" y1="1006" x2="1330" y2="1006"/><line x1="899" y1="1076" x2="1330" y2="1076"/><line x1="968" y1="1000" x2="968" y2="1146"/><line x1="1037" y1="1000" x2="1037" y2="1146"/><line x1="1105" y1="1000" x2="1105" y2="1146"/><line x1="1174" y1="1000" x2="1174" y2="1146"/><line x1="1242" y1="1000" x2="1242" y2="1146"/><line x1="1311" y1="1000" x2="1311" y2="1146"/></g>
    <line x1="899" y1="1000" x2="899" y2="1146" stroke="#999"/><line x1="899" y1="1146" x2="1330" y2="1146" stroke="#999"/>
    <g text-anchor="end"><text x="893" y="1009">10</text><text x="893" y="1080">5</text><text x="893" y="1150">0</text></g>
    <g text-anchor="middle"><text x="899" y="1163">0</text><text x="968" y="1163">5</text><text x="1037" y="1163">10</text><text x="1105" y="1163">15</text><text x="1174" y="1163">20</text><text x="1242" y="1163">25</text><text x="1311" y="1163">30</text></g>
    <g fill="#f6a623">
      <rect x="896" y="1129" width="6" height="17"/><rect x="910" y="1115" width="6" height="31"/><rect x="924" y="1101" width="6" height="45"/><rect x="937" y="1087" width="6" height="59"/><rect x="951" y="1073" width="6" height="73"/><rect x="965" y="1087" width="6" height="59"/><rect x="979" y="1101" width="6" height="45"/><rect x="992" y="1101" width="6" height="45"/><rect x="1006" y="1087" width="6" height="59"/><rect x="1020" y="1073" width="6" height="73"/><rect x="1034" y="1073" width="6" height="73"/><rect x="1047" y="1059" width="6" height="87"/><rect x="1061" y="1059" width="6" height="87"/><rect x="1075" y="1073" width="6" height="73"/><rect x="1089" y="1073" width="6" height="73"/><rect x="1102" y="1087" width="6" height="59"/><rect x="1116" y="1059" width="6" height="87"/><rect x="1130" y="1073" width="6" height="73"/><rect x="1144" y="1087" width="6" height="59"/><rect x="1157" y="1101" width="6" height="45"/><rect x="1171" y="1115" width="6" height="31"/><rect x="1185" y="1129" width="6" height="17"/><rect x="1199" y="1115" width="6" height="31"/><rect x="1212" y="1115" width="6" height="31"/><rect x="1226" y="1101" width="6" height="45"/><rect x="1240" y="1087" width="6" height="59"/><rect x="1254" y="1073" width="6" height="73"/><rect x="1267" y="1059" width="6" height="87"/><rect x="1281" y="1073" width="6" height="73"/><rect x="1295" y="1087" width="6" height="59"/><rect x="1308" y="1101" width="6" height="45"/><rect x="1322" y="1115" width="6" height="31"/>
    </g>
    <polyline points="899,1076 968,1062 1050,1019 1133,1032 1188,1062 1270,1034 1325,1090" fill="none" stroke="#a6d86b"/>
    <g fill="#fff" stroke="#a6d86b"><circle cx="899" cy="1076" r="3"/><circle cx="968" cy="1062" r="3"/><circle cx="1050" cy="1019" r="3"/><circle cx="1133" cy="1032" r="3"/><circle cx="1188" cy="1062" r="3"/><circle cx="1270" cy="1034" r="3"/><circle cx="1325" cy="1090" r="3"/></g>
  </svg>
</section>

<div class="abs stat" style="left:868px;top:1225px"><h4>JOBS</h4><span>1000 <svg width="12" height="12"><circle cx="6" cy="6" r="6" fill="#4caf50"/><path d="M6 3l3 4H3z" fill="#fff"/></svg></span></div>
<div class="abs stat" style="left:1034px;top:1225px"><h4>CUSTOMERS</h4><span>11,000 <svg width="12" height="12"><circle cx="6" cy="6" r="6" fill="#e53935"/><path d="M6 9L3 5h6z" fill="#fff"/></svg></span></div>
<div class="abs stat" style="left:1203px;top:1225px"><h4>REVENUE</h4><span>55.89% <svg width="12" height="12"><circle cx="6" cy="6" r="6" fill="#3ab0e2"/><path d="M6 3l3 4H3z" fill="#fff"/></svg></span></div>
<div class="abs stat" style="left:868px;top:1305px"><h4>REPORTS</h4><span>125 <svg width="12" height="12"><circle cx="6" cy="6" r="6" fill="#3ab0e2"/><path d="M6 9L3 5h6z" fill="#fff"/></svg></span></div>
<div class="abs stat" style="left:1034px;top:1305px"><h4>TICKETS</h4><span>80.99% <svg width="12" height="12"><circle cx="6" cy="6" r="6" fill="#4caf50"/><path d="M6 3l3 4H3z" fill="#fff"/></svg></span></div>
<div class="abs stat" style="left:1203px;top:1305px"><h4>FILES</h4><span>30</span></div>

<div class="abs footer">© 2014 Vomil Brixton Solutions. | Privacy Policy | All rights reserved</div>
</div>
</body>
</html>
```